Business card needed for home based pen making business.

I'm after a business card that's a bit more than an off the shelf card. I do like the idea of a card split horizontal with different colours used. A third colour is to be used for the business name and if need a forth for the other details.

I don't have a logo and will pay extra for one ($150 extra). I mainly make pens and seam rippers (stitch unpicks). The logo may be used for a website in future, as will the colours so please provide the colour codes and font type.

I'd like the business name in an easy to read script font at the top (with logo if you have one) and the other details to the bottom left hand side. I'll leave it up to you to match the script to the font used for the other details.

I'd like to keep a triangular balance to the card so something like a siloet of pot containing pens on the bottom right could be used to balance it out. There my ideas I want to see your.

Business name: Quill & Co
Email address: quillandco@mailbox-example.net
Contact: Trevor
Phone: 0412 555 874
No address is to be used on card.

Target Market(s)

Wide variety of people visiting craft markets. Age range 30+.

Industry/Entity Type

Business

Contact Information for Business Card

Quill & Co

Font styles to use
Script

Colors
f0ecf4
3277b5
3176b5

Requirements
Must have
• Contact: Trevor
• Phone: 0412 555 874
• Email address: quillandco@mailbox-example.net
Nice to have
• An icon and/or graphics depicting pens and seam rippers..
Should not have
• I don't want icon/ graphic to be a crossed pen and seam ripper.

```html
<!DOCTYPE html>
<html lang="en">
<head>
<meta charset="utf-8">
<title>Quill &amp; Co — Business Card</title>
<link rel="stylesheet" href="https://fonts.googleapis.com/css2?family=Kaushan+Script&family=Montserrat:wght@400;500&display=swap">
<style>
  :root {
    --page: #e9e6ec;
    --paper: #f0ecf4;
    --paper-light: #fbfafc;
    --blue: #3277b5;
    --blue-deep: #2a69a6;
    --blue-light: #4ea3d8;
    --band: #343638;
    --ink: #1c1c1c;
    --white: #ffffff;
  }
  * { box-sizing: border-box; margin: 0; padding: 0; }
  html, body {
    width: 734px; height: 1200px; overflow: hidden;
    background: var(--page);
    font-family: "Montserrat", Arial, sans-serif;
  }
  .sheet {
    width: 734px; height: 1200px;
    display: flex; align-items: center; justify-content: center; gap: 34px;
  }
  .card {
    position: relative;
    width: 318px; height: 556px;
    border-radius: 16px;
    overflow: hidden;
    box-shadow: 0 8px 24px rgba(0,0,0,.18);
  }

  /* Front */
  .card-front { background: var(--blue); }
  .front-head {
    position: absolute; left: 0; top: 0; width: 100%; height: 250px;
    background: linear-gradient(180deg, var(--paper-light), var(--paper));
    display: flex; align-items: center; justify-content: center; gap: 12px;
  }
  .front-head .corner-tab {
    position: absolute; right: 0; top: 0; width: 70px; height: 28px;
    background: var(--blue-light); border-bottom-left-radius: 6px;
  }
  .brand-mark {
    width: 30px; height: 30px; border-radius: 50%;
    background: var(--blue); flex: none;
  }
  .brand-name {
    font-family: "Kaushan Script", cursive;
    font-size: 44px; line-height: 1;
    color: var(--ink);
  }
  .name-band {
    position: absolute; left: 0; top: 250px; width: 100%; height: 48px;
    background: var(--band);
    display: flex; align-items: center; justify-content: center;
  }
  .contact-name {
    color: var(--white); font-size: 22px; letter-spacing: 2px; font-weight: 400;
    padding-left: 40px;
  }
  .contact-list {
    position: absolute; left: 0; top: 298px; width: 100%; height: 258px;
    background: linear-gradient(160deg, var(--blue-light) 0%, var(--blue) 70%, var(--blue-deep) 100%);
    list-style: none;
  }
  .contact-list::before {
    content: ""; position: absolute; left: 0; top: 0; width: 60px; height: 100%;
    background: rgba(255,255,255,.14);
  }
  .contact-row {
    position: relative; height: 56px;
    display: flex; align-items: center;
    border-bottom: 1.5px solid rgba(255,255,255,.85);
  }
  .contact-row:last-child { border-bottom: none; }
  .contact-icon {
    width: 60px; display: flex; justify-content: center; flex: none;
  }
  .contact-icon svg { width: 22px; height: 22px; fill: var(--white); }
  .contact-text {
    color: var(--white); font-size: 12.5px; letter-spacing: .6px; padding-left: 12px;
  }
  .social-box {
    width: 18px; height: 18px; border-radius: 3px; background: rgba(255,255,255,.75);
  }

  /* Back */
  .card-back {
    background: linear-gradient(150deg, var(--blue-light) 0%, var(--blue) 55%, var(--blue-deep) 100%);
    display: flex; flex-direction: column; align-items: center; justify-content: center; gap: 18px;
  }
  .card-back .brand-mark {
    width: 84px; height: 84px; background: none; border: 3px solid var(--white);
  }
  .card-back .brand-name { color: var(--white); font-size: 50px; }
</style>
</head>
<body>
<main class="sheet">

  <section class="card card-front" aria-label="Card front">
    <header class="front-head">
      <span class="corner-tab"></span>
      <span class="brand-mark" aria-hidden="true"></span>
      <span class="brand-name">Quill &amp; Co</span>
    </header>
    <div class="name-band"><span class="contact-name">Trevor</span></div>
    <ul class="contact-list">
      <li class="contact-row">
        <span class="contact-icon"><svg viewBox="0 0 24 24" aria-hidden="true"><path d="M6.6 10.8a15.1 15.1 0 0 0 6.6 6.6l2.2-2.2a1 1 0 0 1 1-.25 11.4 11.4 0 0 0 3.6.57 1 1 0 0 1 1 1V20a1 1 0 0 1-1 1A17 17 0 0 1 3 4a1 1 0 0 1 1-1h3.5a1 1 0 0 1 1 1c0 1.25.2 2.45.57 3.57a1 1 0 0 1-.25 1z"/></svg></span>
        <span class="contact-text">0412 555 874</span>
      </li>
      <li class="contact-row">
        <span class="contact-icon"><svg viewBox="0 0 24 24" aria-hidden="true"><path d="M2 5h20v14H2z M3.5 6.5 12 13l8.5-6.5" fill="none" stroke="#fff" stroke-width="1.8"/></svg></span>
        <span class="contact-text">quillandco@mailbox-example.net</span>
      </li>
      <li class="contact-row">
        <span class="contact-icon"><svg viewBox="0 0 24 24" aria-hidden="true"><g fill="none" stroke="#fff" stroke-width="1.6"><circle cx="12" cy="12" r="9"/><ellipse cx="12" cy="12" rx="4" ry="9"/><path d="M3 12h18M5 7h14M5 17h14"/></g></svg></span>
        <span class="contact-text">www.quillandco-example.net</span>
      </li>
      <li class="contact-row">
        <span class="contact-icon"><span class="social-box" aria-hidden="true"></span></span>
        <span class="contact-text">Quill &amp; Co</span>
      </li>
    </ul>
  </section>

  <section class="card card-back" aria-label="Card back">
    <span class="brand-mark" aria-hidden="true"></span>
    <span class="brand-name">Quill &amp; Co</span>
  </section>

</main>
</body>
</html>
```